Exterior cleaning company requires a eye catching a5 leaflet

we need some updated leaflet designs, a5 folded, we are targeting all exterior cleaning contracts, including roof cleaning & treatment, render cleaning & Treatment, driveways, block paving cleaning using the latest in low pressure cleaning technologies along side high pressure jetwashing. gutter clearance and flushing, water fed telescopic pole window cleaning of difficult to reach windows and high buildings. our website : www.tkbellowsec.co.uk facebook page: https://www.facebook.com/tkbellowsexteriorcareltd Instagram: https://www.instagram.com/tkbellowsec/ a quick google search of roof cleaning, soft washing etc will provide results of what we are doing

Target Market(s)

home owners, commercial clients

Font styles to use
Serif
Sans Serif

Requirements
Must have
• A5 Landscape folded leaflet, front page with company information and bullet points of main works : window & conservatory cleaning, roof cleaning & treatment, Render cleaning & treatment, pressure washing, soft washing, gutter clearing, pressure washing of patios, driveways, gutters, fascias (more info can be provided on techniques etc if required)

```html
<!DOCTYPE html>
<html lang="en">
<head>
<meta charset="utf-8">
<title>Kestrel Brook Exterior Care – A5 Folded Leaflet</title>
<link href="https://fonts.googleapis.com/css2?family=Montserrat:wght@300;400;500;600;700;800;900&display=swap" rel="stylesheet">
<style>
:root{
  --backdrop:#e4e4e4;
  --paper:#f5f5f4;
  --ink:#1b1b1b;
  --ink-soft:#555;
  --rule:#2a2a2a;
  --sky:#b8bcc0;
  --brick:#7a4634;
  --grass:#5f9a3c;
  --stone:#b9a489;
  --slate:#3a3d44;
}
*{box-sizing:border-box;margin:0;padding:0}
html,body{width:1200px;height:3600px;overflow:hidden}
body{
  background:var(--backdrop);
  font-family:"Montserrat",sans-serif;
  color:var(--ink);
  display:flex;flex-direction:column;align-items:center;justify-content:space-evenly;
}
/* panels */
.panel{position:relative;width:550px;height:560px;overflow:hidden;background:var(--paper)}
.spread{display:flex;width:1100px;box-shadow:0 6px 24px rgba(0,0,0,.12)}
.spread .panel + .panel{border-left:1px solid #dcdcdc}
.cover-stage{width:798px;height:812px;position:relative;box-shadow:0 6px 24px rgba(0,0,0,.12)}
.cover-stage .panel{position:absolute;left:0;top:0;transform:scale(1.45);transform-origin:0 0}

/* photo placeholders */
.photo{position:absolute;background:linear-gradient(180deg,var(--sky),#8d8f92)}
.photo--round{border-radius:50%}
.ring{position:absolute;border-radius:50%;border:1.5px solid var(--rule);border-top-color:transparent;border-right-color:transparent}

/* brand lockup */
.brand{position:absolute;display:flex;align-items:center;gap:10px}
.brand__mark{width:46px;height:46px;border:1.5px solid var(--ink);border-radius:50%}
.brand__name{font-weight:800;font-size:16px;line-height:1}
.brand__sub{font-weight:800;font-size:8.5px;line-height:1.3}

/* front */
.headline{position:absolute;left:78px;top:270px;text-transform:uppercase}
.headline__light{font-weight:400;font-size:22px;line-height:1.02;letter-spacing:.5px}
.headline__bold{font-weight:900;font-size:38px;line-height:.92;letter-spacing:.5px}
.headline__tag{font-weight:400;font-size:12.5px;letter-spacing:.8px;margin-top:3px}
.headline__rule{width:70px;height:3px;background:var(--ink);margin-top:6px}
.service-strip{position:absolute;left:40px;right:30px;top:448px;display:flex;flex-wrap:wrap;row-gap:8px;font-size:9.5px;text-transform:uppercase;letter-spacing:.4px}
.service-strip li{list-style:none;padding:0 7px;border-left:1.5px solid var(--ink);line-height:1}
.service-strip li:first-child,.service-strip li.wrap{border-left:none;padding-left:0}

/* back */
.area{position:absolute;left:40px;right:40px;top:170px;text-align:center}
.area__title{font-size:16px;font-weight:400;text-transform:uppercase;letter-spacing:.5px}
.area__title b{font-weight:800}
.area__rule{width:110px;height:2px;background:var(--ink);margin:6px auto 18px}
.area__towns{display:flex;flex-wrap:wrap;justify-content:center;row-gap:9px;font-size:10px;text-transform:uppercase;letter-spacing:.5px}
.area__towns li{list-style:none;padding:0 8px;border-left:1.5px solid var(--ink);line-height:1}
.area__towns li.first{border-left:none}
.contact{position:absolute;left:290px;top:400px;border-left:2px solid var(--ink);padding-left:14px;font-size:10px;text-transform:uppercase;display:flex;flex-direction:column;gap:8px}
.contact__row{display:flex;align-items:center;gap:7px}
.contact__row svg{width:13px;height:13px}

/* inside */
.section-title{position:absolute;font-size:17px;font-weight:400;text-transform:uppercase;letter-spacing:.3px}
.section-title b{font-weight:800}
.about-copy{position:absolute;left:250px;top:78px;width:275px;font-size:8.6px;line-height:1.45;color:var(--ink-soft);display:flex;flex-direction:column;gap:7px}
.photo-row{position:absolute;display:flex;gap:10px}
.photo-row .photo{position:static;width:116px;height:108px}
.services{position:absolute;left:28px;right:24px;top:212px;display:grid;grid-template-columns:1fr 1fr;column-gap:26px;row-gap:18px}
.service{display:flex;gap:9px}
.service__icon{flex:none;width:22px;height:22px;border-radius:50%;background:var(--ink);display:flex;align-items:center;justify-content:center}
.service__icon svg{width:12px;height:12px}
.service__name{font-size:9.5px;font-weight:800;text-transform:uppercase;margin-bottom:3px}
.service__text{font-size:8.4px;line-height:1.4;color:var(--ink-soft)}
.title-rule{position:absolute;height:2px;background:var(--ink)}
</style>
</head>
<body>

<!-- Front cover -->
<div class="cover-stage">
  <section class="panel panel--front">
    <div class="photo photo--round" style="left:205px;top:-305px;width:560px;height:560px;background:linear-gradient(180deg,var(--sky) 0 52%,var(--brick) 52% 80%,var(--grass) 80%)" role="img" aria-label="Photo of a cleaner using a water fed pole on a modern brick house with a glass balcony"></div>
    <div class="ring" style="left:188px;top:-322px;width:594px;height:594px;transform:rotate(-10deg)"></div>
    <div class="brand" style="left:36px;top:188px">
      <span class="brand__mark"></span>
      <div><div class="brand__name">Kestrel Brook</div><div class="brand__sub">Exterior Care Ltd<br>Tel: 01632 960 418</div></div>
    </div>
    <div class="headline">
      <div class="headline__light">Most Reliable<br>&amp; Professional</div>
      <div class="headline__bold">Cleaning<br>Services</div>
      <div class="headline__tag">With 10 Years Experience</div>
      <div class="headline__rule"></div>
    </div>
    <ul class="service-strip">
      <li>Window &amp; Conservatory Cleaning</li><li>Roof Cleaning &amp; Treatment</li><li>Render Cleaning &amp; Treatment</li>
      <li class="wrap">Pressure Washing</li><li>Soft Washing</li><li>Gutter Clearing</li><li>Pressure Washing of Patios</li>
      <li class="wrap">Driveways, Gutters</li><li>Fascias</li><li>&amp; Many More</li>
    </ul>
  </section>
</div>

<!-- Outer spread -->
<div class="spread">
  <section class="panel panel--back">
    <div class="area">
      <h2 class="area__title">Our <b>Service Area</b></h2>
      <div class="area__rule"></div>
      <ul class="area__towns">
        <li class="first">Southport</li><li>Liverpool</li><li>Ormskirk</li><li>Banks</li><li>Hesketh Bank</li><li>Halsall</li>
        <li class="first">Scarisbrick</li><li>Tarleton</li><li>Skelmersdale</li><li>Burscough</li><li>Aughton</li><li>Formby</li>
      </ul>
    </div>
    <div class="brand" style="left:36px;top:470px">
      <span class="brand__mark"></span>
      <div><div class="brand__name">Kestrel Brook</div><div class="brand__sub">Exterior Care Ltd<br>Tel: 01632 960 418</div></div>
    </div>
    <div class="contact">
      <div class="contact__row"><svg viewBox="0 0 16 16"><circle cx="8" cy="8" r="7.2" fill="none" stroke="#1b1b1b"/><path d="M5.5 4.5l1.5 0 .7 2-1 .8a5 5 0 0 0 2 2l.8-1 2 .7v1.5c0 .5-.5 1-1 1A6 6 0 0 1 4.5 5.5c0-.5.5-1 1-1z" fill="#1b1b1b"/></svg>01632 960 418</div>
      <div class="contact__row"><svg viewBox="0 0 16 16"><circle cx="8" cy="8" r="7.2" fill="none" stroke="#1b1b1b"/><rect x="4" y="5.5" width="8" height="5.5" fill="none" stroke="#1b1b1b"/><path d="M4 5.5l4 3 4-3" fill="none" stroke="#1b1b1b"/></svg>info@kestrelbrook.co.uk</div>
      <div class="contact__row"><svg viewBox="0 0 16 16"><circle cx="8" cy="8" r="7.2" fill="none" stroke="#1b1b1b"/><path d="M8 12.5s-3-3.2-3-5.3a3 3 0 0 1 6 0c0 2.1-3 5.3-3 5.3z" fill="#1b1b1b"/><circle cx="8" cy="7.2" r="1" fill="#fff"/></svg>27 Linden Walk, Southport, PR9 4LT</div>
    </div>
  </section>

  <section class="panel panel--front">
    <div class="photo photo--round" style="left:205px;top:-305px;width:560px;height:560px;background:linear-gradient(180deg,var(--sky) 0 52%,var(--brick) 52% 80%,var(--grass) 80%)" role="img" aria-label="Photo of a cleaner using a water fed pole on a modern brick house with a glass balcony"></div>
    <div class="ring" style="left:188px;top:-322px;width:594px;height:594px;transform:rotate(-10deg)"></div>
    <div class="brand" style="left:36px;top:188px">
      <span class="brand__mark"></span>
      <div><div class="brand__name">Kestrel Brook</div><div class="brand__sub">Exterior Care Ltd<br>Tel: 01632 960 418</div></div>
    </div>
    <div class="headline">
      <div class="headline__light">Most Reliable<br>&amp; Professional</div>
      <div class="headline__bold">Cleaning<br>Services</div>
      <div class="headline__tag">With 10 Years Experience</div>
      <div class="headline__rule"></div>
    </div>
    <ul class="service-strip">
      <li>Window &amp; Conservatory Cleaning</li><li>Roof Cleaning &amp; Treatment</li><li>Render Cleaning &amp; Treatment</li>
      <li class="wrap">Pressure Washing</li><li>Soft Washing</li><li>Gutter Clearing</li><li>Pressure Washing of Patios</li>
      <li class="wrap">Driveways, Gutters</li><li>Fascias</li><li>&amp; Many More</li>
    </ul>
  </section>
</div>

<!-- Inner spread -->
<div class="spread">
  <section class="panel panel--about">
    <div class="photo photo--round" style="left:-110px;top:-130px;width:340px;height:340px;background:linear-gradient(180deg,#9aa49a 0 45%,var(--stone) 45%)" role="img" aria-label="Photo of a cleaner washing glass balustrades on a stone patio"></div>
    <div class="ring" style="left:-124px;top:-144px;width:368px;height:368px;transform:rotate(-30deg)"></div>
    <h2 class="section-title" style="left:250px;top:40px">About <b>Kestrel Brook</b></h2>
    <div class="title-rule" style="left:250px;top:64px;width:60px"></div>
    <div class="about-copy">
      <p>Kestrel Brook Exterior Care is a family run cleaning business serving homes and businesses across the region, built on honest prices, careful work and friendly service.</p>
      <p>We use pure water fed pole systems to reach high and awkward windows safely, leaving glass, frames and sills spotless without ladders on your property.</p>
      <p>Our team is fully insured and trained in soft washing, roof treatment and render care, so every surface is cleaned with the right method.</p>
      <p>Our window cleaning rounds cover most local areas. Please call to book a free quote today.</p>
    </div>
    <div class="photo-row" style="left:24px;top:420px">
      <div class="photo" style="background:linear-gradient(180deg,#a9adb1,var(--brick))" role="img" aria-label="Photo of a brick apartment building with a white van"></div>
      <div class="photo" style="background:linear-gradient(180deg,#6b5a4a,#8c7a66)" role="img" aria-label="Photo of a shop interior with clean windows"></div>
      <div class="photo" style="background:linear-gradient(180deg,#5a86b8 0 55%,var(--grass) 55%)" role="img" aria-label="Photo of a commercial building front with lawn"></div>
      <div class="photo" style="background:linear-gradient(180deg,#c8c8c8,var(--slate))" role="img" aria-label="Photo of a rooftop solar panel array"></div>
    </div>
  </section>

  <section class="panel panel--services">
    <div class="photo-row" style="left:24px;top:30px">
      <div class="photo" style="background:linear-gradient(180deg,#9a9a9a,#3c3c3c)" role="img" aria-label="Photo of a clean gym floor with windows"></div>
      <div class="photo" style="background:linear-gradient(180deg,#a4553f,#7a3b2c)" role="img" aria-label="Photo of freshly washed block paving"></div>
      <div class="photo" style="background:linear-gradient(180deg,#c9ccce,#7b7f84)" role="img" aria-label="Photo of a glazed shop front"></div>
      <div class="photo" style="background:linear-gradient(180deg,#98a2a8,#22262b)" role="img" aria-label="Photo of the company van"></div>
    </div>
    <h2 class="section-title" style="left:28px;top:160px">Services <b>We Offered</b></h2>
    <div class="title-rule" style="left:245px;top:172px;width:280px"></div>
    <div class="services">
      <div class="service"><span class="service__icon"><svg viewBox="0 0 12 12"><path d="M2 6.3l2.5 2.5L10 3.2" fill="none" stroke="#fff" stroke-width="1.8"/></svg></span><div><div class="service__name">External Windows</div><p class="service__text">Pure water pole cleaning for frames, sills and glass up to four storeys high.</p></div></div>
      <div class="service"><span class="service__icon"><svg viewBox="0 0 12 12"><path d="M2 6.3l2.5 2.5L10 3.2" fill="none" stroke="#fff" stroke-width="1.8"/></svg></span><div><div class="service__name">Fascias &amp; Gutters</div><p class="service__text">Soffits, fascias and gutter faces washed back to a bright, like new finish.</p></div></div>
      <div class="service"><span class="service__icon"><svg viewBox="0 0 12 12"><path d="M2 6.3l2.5 2.5L10 3.2" fill="none" stroke="#fff" stroke-width="1.8"/></svg></span><div><div class="service__name">Internal Windows</div><p class="service__text">Careful inside cleaning with drop sheets and streak free finish on every pane.</p></div></div>
      <div class="service"><span class="service__icon"><svg viewBox="0 0 12 12"><path d="M2 6.3l2.5 2.5L10 3.2" fill="none" stroke="#fff" stroke-width="1.8"/></svg></span><div><div class="service__name">Driveways &amp; Patios</div><p class="service__text">Block paving, stone and concrete jet washed, re-sanded and sealed on request.</p></div></div>
      <div class="service"><span class="service__icon"><svg viewBox="0 0 12 12"><path d="M2 6.3l2.5 2.5L10 3.2" fill="none" stroke="#fff" stroke-width="1.8"/></svg></span><div><div class="service__name">Conservatory Roofs</div><p class="service__text">Moss, algae and dirt removed gently from glass and polycarbonate roof panels.</p></div></div>
      <div class="service"><span class="service__icon"><svg viewBox="0 0 12 12"><path d="M2 6.3l2.5 2.5L10 3.2" fill="none" stroke="#fff" stroke-width="1.8"/></svg></span><div><div class="service__name">Gutter Cleaning</div><p class="service__text">Gutters cleared by vacuum from the ground and downpipes flushed to prevent leaks.</p></div></div>
      <div class="service"><span class="service__icon"><svg viewBox="0 0 12 12"><path d="M2 6.3l2.5 2.5L10 3.2" fill="none" stroke="#fff" stroke-width="1.8"/></svg></span><div><div class="service__name">Solar Panels</div><p class="service__text">Clean panels can produce more power, so regular washing pays for itself.</p></div></div>
      <div class="service"><span class="service__icon"><svg viewBox="0 0 12 12"><path d="M2 6.3l2.5 2.5L10 3.2" fill="none" stroke="#fff" stroke-width="1.8"/></svg></span><div><div class="service__name">Pressure Washing</div><p class="service__text">We offer a wide range of pressure washing services from garden furniture to house walls at competitive prices. Cleaning and restoration of all hard surfaces in both the domestic and commercial market.</p></div></div>
    </div>
  </section>
</div>

</body>
</html>
```